Life Insurance For Real Life

this is a statement I came up with - I am selling insurance based on the fact that I have gone through exactly what insurance can do for everyone: <br/>It’s not “just insurance” it’s a life jacket when you can’t stop the boat from sinking. Think about it…. Will you be safe? Will your family be safe if tragedy takes you away? Who will pay all the expenses if you or your spouse are not here anymore? Believe me, I know. Let me help you take care of the ones you love. <br/>Call me: 555-218-6093, Mae Lin Trost <br/>“REAL LIFE EXPERIENCE FOR REAL LIFE”<br/>

Target Market(s)

New Jersey (USA) seniors ages 65-80.

Industry/Entity Type

Insurance

Colors

Designer to choose colors to be used in the design.

Requirements
Must have
• Good photo of family people who look like they are concerned with family matters - I do not want my name or company name on the first page. I also want a button they can press and get to a second page where they enter contact info and include a email us now type button with a direct email from their device to me.
Nice to have
• maybe an interracial couple with 2-3 kids and a mid-life aged couple - 40-something or so - people who look like they want to make sure their family is safe and taken care of. I am looking to play on emotions to get people to think.
Should not have
• should not have my name or company name

```html
<!DOCTYPE html>
<html lang="en">
<head>
<meta charset="utf-8">
<title>Life Insurance For Real Life</title>
<link href="https://fonts.googleapis.com/css2?family=Poppins:wght@400;500;600&family=Satisfy&display=swap" rel="stylesheet">
<style>
  :root {
    --page-bg: #212b3c;
    --card-bg: #ffffff;
    --slate: #3f5673;
    --green: #1fb80f;
    --ink: #0d0d0d;
    --red: #f20d0d;
    --script-grey: #6d6d6d;
    --btn-slate-top: #5a7394;
    --btn-slate-bottom: #3a5170;
    --btn-green-top: #35d41f;
    --btn-green-bottom: #14a806;
  }
  * { box-sizing: border-box; margin: 0; padding: 0; }
  html, body { width: 1200px; height: 1200px; overflow: hidden; }
  body {
    background: var(--page-bg);
    font-family: "Poppins", sans-serif;
    position: relative;
  }
  .banner {
    position: absolute;
    left: 79px; top: 302px;
    width: 1042px; height: 598px;
    background: var(--card-bg);
    overflow: hidden;
  }
  .family-photo {
    position: absolute;
    left: 470px; top: 0;
    width: 572px; height: 598px;
    background:
      radial-gradient(ellipse at 70% 35%, #e6c3ae 0%, rgba(230,195,174,0) 45%),
      radial-gradient(ellipse at 90% 75%, #e9c6d6 0%, rgba(233,198,214,0) 40%),
      radial-gradient(ellipse at 40% 70%, #9fa3aa 0%, rgba(159,163,170,0) 50%),
      linear-gradient(90deg, rgba(255,255,255,1) 0%, rgba(240,236,234,0.6) 30%, #d9cfca 100%);
  }
  .copy { position: absolute; left: 44px; }
  .intro {
    top: 28px;
    color: var(--slate);
    font-size: 21px;
    line-height: 30px;
  }
  .intro .lead { font-size: 26px; }
  .metaphor {
    top: 130px;
    color: var(--green);
    font-weight: 500;
    font-size: 23px;
    line-height: 32px;
  }
  .question {
    top: 198px;
    color: var(--ink);
    font-weight: 600;
    font-size: 30px;
    line-height: 39px;
  }
  .expenses {
    top: 325px;
    color: var(--green);
    font-size: 23px;
    line-height: 33px;
  }
  .promise {
    top: 393px;
    color: var(--slate);
    font-weight: 500;
    font-size: 22px;
    line-height: 35px;
  }
  .promise .strong { font-size: 26px; }
  .promise .love { color: var(--red); }
  .btn {
    position: absolute;
    top: 480px; height: 46px;
    border-radius: 23px;
    color: #fff;
    display: flex; align-items: center; justify-content: center;
    text-decoration: none;
  }
  .btn-email {
    left: 44px; width: 253px;
    background: linear-gradient(var(--btn-slate-top), var(--btn-slate-bottom));
    font-size: 27px; font-weight: 500;
  }
  .btn-call {
    left: 308px; width: 345px;
    background: linear-gradient(var(--btn-green-top), var(--btn-green-bottom));
    font-size: 24px; font-weight: 600;
  }
  .tagline {
    position: absolute;
    left: 44px; top: 540px;
    font-family: "Satisfy", cursive;
    color: var(--script-grey);
    font-size: 32px;
  }
</style>
</head>
<body>
  <section class="banner">
    <div class="family-photo" role="img" aria-label="Smiling family of four: father carrying a son on his back, mother and daughter hugging beside him"></div>

    <p class="copy intro"><span class="lead">I am selling insurance based on the fact</span><br>that I have gone through exactly&nbsp; what insurance<br>can do for everyone:</p>
    <p class="copy metaphor">It’s not “just insurance” it’s a life jacket when<br>you can’t stop the boat from sinking.</p>
    <p class="copy question">Think about it…. Will you be safe?<br>Will your family be safe if tragedy<br>takes you away?</p>
    <p class="copy expenses">Who will pay all the expenses if you<br>or your spouse are not here anymore?</p>
    <p class="copy promise"><span class="strong">Believe me, I know.</span> Let me help you<br>take care of the ones <span class="love">you love.</span></p>

    <a class="btn btn-email" href="#contact">Email us now</a>
    <a class="btn btn-call" href="tel:5552186093">CALL ME : 555-218-6093</a>

    <p class="tagline">Real life experience for real life</p>
  </section>
</body>
</html>
```